Brochure layout for a small country church

St. Wendel is a small country church located on the central coast of CA. Last year our priest retired, and we are in the process of seeking a new church leader. To support our search process, we created a profile brochure that describes who we are in words and images.

The copy has been carefully written and fully edited, and we have gathered, tagged and foldered high-resolution images. We now need a person with your talents to arrange the words and pictures for us!

This document, which we call a 'profile' but is actually a brochure, will be in PDF format, size 8.5x11, for web display and local printing only. It will be posted on a national database and be shared with candidates by email and on our website. We do not intend to reproduce this on paper, though we expect some users will print pages on their printers.

Here is a Cloudpail link to access the copy, images and layout instructions:
https://www.cloudpail-share.net/sh/k3rtezn7wqa8u2x/BBDQLM-17h88_pR4TUwnXoEbz

The layout instructions include specific information on image placement, and gives you much flexibility to arrange the copy/images the way you think looks best. All we ask is that you do not change the copy.

Images may be processed, cropped, inverted, enhanced … whatever you think looks right. We tried to give you the largest images possible, so you can get good resolution on the page.

Please do not let the length of the document concern you … you can cut/paste the copy, using any serif font that matches the look/feel of our church, and all of the images have been tagged and folder addressed in the document so you know where to find them. Page count does not matter as long as it looks good, and once you start laying out the pages it should not take long to finish. We just need someone with your design skills to make it look good!

As we stated in the copy narrative, we are a warm, loving and inclusive parish that is humble, happy and grateful for the many blessings we have. Our greatest quality is our people. In your design work, anything you can do to bring forward these values will be appreciated.

If you have any questions, please do not hesitate to contact me (Gordon Pelley/gordon@gordonpelley-mail.net) and I will answer them for you right away.

Thank you for considering our brochure project, and we look forward to your submission.

Industry/Entity Type

Church

```html
<!DOCTYPE html>
<html lang="en">
<head>
<meta charset="utf-8">
<title>Parish Profile – St. Wendel the Apostle</title>
<link href="https://fonts.googleapis.com/css2?family=Lato:wght@300;400;900&display=swap" rel="stylesheet">
<style>
  :root {
    --paper: #ddd6cc;
    --paper-light: #e8e3db;
    --ink: #4a2a16;
    --drape-dark: #3b2213;
    --drape-mid: #6a3a1a;
    --sky: #a9c8e2;
    --foliage: #4f7a3a;
    --wall: #8fa9d4;
    --tower: #f2ede2;
  }
  * { margin: 0; padding: 0; box-sizing: border-box; }
  html, body { width: 927px; height: 1200px; overflow: hidden; }
  body {
    background: radial-gradient(ellipse at 50% 75%, var(--paper-light), var(--paper));
    font-family: "Lato", sans-serif;
    color: var(--ink);
    position: relative;
  }
  .cover {
    position: absolute; left: 0; top: 0; width: 927px; height: 760px;
  }
  .cover-text {
    position: absolute; left: 0; right: 0;
    text-align: center; line-height: 1; white-space: nowrap;
  }
  .kicker { top: 821px; font-size: 46px; font-weight: 300; }
  .parish-name { top: 884px; font-size: 68px; font-weight: 900; letter-spacing: -0.5px; }
  .location { top: 966px; font-size: 46px; font-weight: 300; }
  .issue-date { top: 1117px; font-size: 36px; font-weight: 300; }
</style>
</head>
<body>
  <svg class="cover" viewBox="0 0 927 760" aria-hidden="false">
    <defs>
      <linearGradient id="art-sides" x1="0" x2="1" y1="0" y2="0">
        <stop offset="0" stop-color="var(--foliage)"/>
        <stop offset="0.22" stop-color="var(--sky)"/>
        <stop offset="0.72" stop-color="var(--sky)"/>
        <stop offset="1" stop-color="var(--foliage)"/>
      </linearGradient>
      <radialGradient id="art-centre" cx="0.48" cy="0.55" r="0.5">
        <stop offset="0" stop-color="var(--tower)"/>
        <stop offset="0.35" stop-color="var(--wall)"/>
        <stop offset="1" stop-color="var(--wall)" stop-opacity="0"/>
      </radialGradient>
      <clipPath id="art-clip">
        <path d="M0,0 H927 V583 C800,598 560,612 463,652 C366,612 127,598 0,583 Z"/>
      </clipPath>
    </defs>
    <g clip-path="url(#art-clip)" role="img" aria-label="Painting of the white church with its red-roofed bell tower among trees under a blue sky">
      <rect width="927" height="660" fill="url(#art-sides)"/>
      <rect width="927" height="660" fill="url(#art-centre)"/>
    </g>
    <path fill="var(--drape-dark)" d="M0,583 C127,598 366,612 463,652 C566,612 800,598 927,583 L927,680 C800,700 560,700 463,652 C366,700 127,700 0,680 Z"/>
    <path fill="var(--drape-mid)" d="M0,680 C127,700 366,700 463,652 C560,700 800,700 927,680 L927,700 C830,740 580,740 463,652 C346,740 97,740 0,700 Z"/>
  </svg>
  <p class="cover-text kicker">PARISH PROFILE</p>
  <h1 class="cover-text parish-name">ST. WENDEL THE APOSTLE</h1>
  <p class="cover-text location">ALDER CREST, CALIFORNIA</p>
  <p class="cover-text issue-date">MAY 2014</p>
</body>
</html>
```